Q&L Summit Holdings Business Cards

Design Business cards in a format where I can change the information and utilize a third party buisness card printing company

Contact Information for Business Card

Want Logo and Name on Back. Looking for Spot UV style shine on Logo. Probably Black background. Want smaller logo on front with contact details. Like rounded edges or something else interesting.

Requirements
Must have
• Strong masculine look.

```html
<!DOCTYPE html>
<html lang="en">
<head>
<meta charset="utf-8">
<title>Q&amp;L Summit Holdings – Business Cards</title>
<link href="https://fonts.googleapis.com/css2?family=Cinzel:wght@400;500&family=EB+Garamond:wght@400&display=swap" rel="stylesheet">
<style>
  :root {
    --backdrop: #2b2b2b;
    --card: #151515;
    --card-edge: #0c0c0c;
    --name-grey: #8c8c8c;
    --detail-grey: #c9c9c9;
    --silver: #dcdcdc;
  }
  * { margin: 0; padding: 0; box-sizing: border-box; }
  html, body {
    width: 1200px;
    height: 960px;
    overflow: hidden;
    background: var(--backdrop);
  }
  .canvas {
    position: relative;
    width: 1200px;
    height: 960px;
  }
  .card {
    position: absolute;
    left: 322px;
    width: 600px;
    height: 344px;
    background: var(--card);
    border: 1px solid var(--card-edge);
    border-radius: 72px 6px 72px 6px;
    box-shadow: 0 6px 18px rgba(0,0,0,0.55);
    text-align: center;
  }
  .card--front { top: 110px; }
  .card--back { top: 493px; }

  .contact__name {
    position: absolute;
    top: 82px;
    width: 100%;
    font-family: "Cinzel", serif;
    font-size: 24px;
    font-weight: 400;
    letter-spacing: 0.5px;
    color: var(--name-grey);
  }
  .contact__title {
    position: absolute;
    top: 110px;
    width: 100%;
    font-family: "Cinzel", serif;
    font-size: 15px;
    font-weight: 500;
    letter-spacing: 1px;
    color: var(--detail-grey);
  }
  .contact__block {
    position: absolute;
    width: 100%;
    font-family: "EB Garamond", serif;
    font-size: 16px;
    line-height: 19px;
    color: var(--detail-grey);
  }
  .contact__address { top: 143px; }
  .contact__lines { top: 197px; }

  .brand-mark {
    position: absolute;
    top: 70px;
    left: 240px;
    width: 108px;
    height: 108px;
    border: 3px solid var(--silver);
  }
  .brand-name {
    position: absolute;
    top: 214px;
    left: 0;
    width: 576px;
    font-family: "Cinzel", serif;
    font-size: 30px;
    font-weight: 500;
    letter-spacing: 0.5px;
    color: var(--silver);
    white-space: nowrap;
  }
</style>
</head>
<body>
<main class="canvas">
  <section class="card card--front" aria-label="Business card front">
    <p class="contact__name">DANIEL REYES</p>
    <p class="contact__title">CEO/FOUNDER</p>
    <p class="contact__block contact__address">1420 Harbor Ridge Road<br>Juneau, Alaska 99801</p>
    <p class="contact__block contact__lines">(P) 555 214 7390<br>(E) daniel@qlsummit.com<br>www.qlsummit.com</p>
  </section>

  <section class="card card--back" aria-label="Business card back">
    <div class="brand-mark" aria-hidden="true"></div>
    <p class="brand-name">Q&amp;L Summit Holdings</p>
  </section>
</main>
</body>
</html>
```